Jornadas Quietud

I want a Catholic flyer, with the Virgen Mary showing aiding, praying, and Jesus carrying the cross, to invite people to a silent retreat. The retreats are monthly. For women, they are Feb. 21, March 21, etc (every third Saturday), and for men they are Feb. 28, March 28, etc (every fourth Saturday). I want each month date to show for both women and men. Our logo should be in there, which is similar to the Holy family icon attached. Also, show that cost is $80, and the place for the retreats is Casa de Reposo, 4175 Marwick Ln, Falls Church, VA and for more information to contact, for women 540-627-1954 and for men 571-482-7105. I will use the flyer for around 4 x 6 or 3 x 5 postcard. Organizers are: Casas de Monte Olvera. The flyer needs to be in spanish "RETIROS EN SILENCIO" and the months should be labeled in Spanish too.

```html
<!DOCTYPE html>
<html lang="es">
<head>
<meta charset="utf-8">
<title>Jornadas Quietud</title>
<link rel="stylesheet" href="https://fonts.googleapis.com/css2?family=Abril+Fatface&family=Poppins:wght@400;500;600;700&display=swap">
<style>
  :root {
    --parchment: #e6cc92;
    --parchment-dark: #c9a25c;
    --wine: #5c1014;
    --ink: #1a1410;
    --band: #7b3b07;
    --gold: #f2b640;
    --pill: #fde4c8;
    --white: #ffffff;
    --line: #5a4630;
  }
  * { box-sizing: border-box; margin: 0; padding: 0; }
  html, body { width: 824px; height: 1200px; overflow: hidden; background: #b8b8b8; }
  .flyer {
    position: relative; width: 824px; height: 1200px; overflow: hidden;
    background: radial-gradient(ellipse at 50% 30%, #f3e2b0 0%, var(--parchment) 45%, var(--parchment-dark) 100%);
    font-family: "Poppins", sans-serif; color: var(--ink);
  }
  .hero-art {
    position: absolute; left: 0; top: 0; width: 824px; height: 640px;
    background:
      radial-gradient(ellipse at 50% 35%, rgba(250,240,170,0.9) 0%, rgba(230,205,130,0.5) 35%, rgba(0,0,0,0) 65%),
      linear-gradient(90deg, #8a6b3e 0%, #c4a56a 30%, #e8d69a 50%, #b49359 72%, #6e4f2a 100%);
    -webkit-mask-image: linear-gradient(180deg, #000 55%, transparent 100%);
            mask-image: linear-gradient(180deg, #000 55%, transparent 100%);
  }
  .organizer {
    position: absolute; left: 0; right: 0; top: 120px;
    display: flex; align-items: center; justify-content: center; gap: 10px;
    font-weight: 600; font-size: 20px; color: var(--wine);
  }
  .organizer .mark { width: 18px; height: 18px; background: var(--wine); }
  .title {
    position: absolute; left: 0; right: 0; top: 238px; text-align: center;
    font-family: "Abril Fatface", serif; color: var(--wine);
    font-size: 96px; line-height: 1; letter-spacing: 1px;
  }
  .subtitle {
    position: absolute; left: 0; right: 0; top: 340px; text-align: center;
    font-family: "Abril Fatface", serif; color: var(--ink); font-size: 46px; line-height: 1;
  }
  .tagline {
    position: absolute; left: 0; right: 0; top: 416px; text-align: center;
    font-size: 32px; font-weight: 400; line-height: 1.2;
  }
  .schedule {
    position: absolute; left: 69px; width: 674px; height: 170px;
    background: var(--band); color: var(--white); text-align: center;
  }
  .schedule.women { top: 499px; }
  .schedule.men { top: 711px; }
  .audience {
    position: absolute; left: 50%; top: -22px; transform: translateX(-50%);
    background: var(--pill); color: var(--ink); border-radius: 22px;
    padding: 6px 22px; font-weight: 600; font-size: 21px; white-space: nowrap;
  }
  .lead { margin-top: 18px; font-weight: 600; font-size: 17px; line-height: 1.4; letter-spacing: 5px; }
  .dates { display: flex; align-items: center; justify-content: center; gap: 20px; margin-top: 2px; }
  .date { display: flex; align-items: flex-end; }
  .day { font-weight: 600; font-size: 76px; line-height: 0.9; color: var(--gold); letter-spacing: -2px; }
  .month { display: flex; flex-direction: column; margin-left: 2px; text-align: left; line-height: 0.9; }
  .month .de { font-weight: 600; font-size: 24px; }
  .month .name { font-weight: 600; font-size: 40px; }
  .and {
    width: 44px; height: 44px; border-radius: 50%; background: var(--white); color: var(--ink);
    display: flex; align-items: center; justify-content: center; font-weight: 600; font-size: 26px; line-height: 1; padding-bottom: 6px;
  }
  .cadence { margin-top: 4px; font-weight: 600; font-size: 24px; line-height: 1.3; color: var(--pill); }
  .cost { position: absolute; left: 51px; top: 916px; display: flex; align-items: flex-start; }
  .cost .label { font-weight: 600; font-size: 29px; line-height: 0.9; margin-top: 8px; }
  .cost .currency { font-weight: 700; font-size: 36px; color: var(--band); margin-left: 8px; margin-top: 6px; }
  .cost .amount { font-weight: 600; font-size: 92px; line-height: 0.95; color: var(--band); letter-spacing: -2px; }
  .divider { position: absolute; left: 351px; top: 905px; width: 1px; height: 118px; background: var(--line); }
  .venue { position: absolute; left: 376px; top: 922px; }
  .venue h3 { font-weight: 600; font-size: 25px; color: var(--band); line-height: 1.1; }
  .venue .address { display: flex; gap: 8px; font-size: 22px; line-height: 1.2; margin-top: 2px; }
  .venue svg { flex: none; margin-top: 5px; }
  .contact {
    position: absolute; left: 51px; top: 1073px; width: 722px; height: 86px;
    border: 1px solid var(--line);
  }
  .contact .heading {
    position: absolute; left: 190px; top: -19px; width: 334px; height: 38px;
    background: #0d0d0d; color: var(--white); border-radius: 10px;
    font-size: 22px; text-align: center; line-height: 38px;
  }
  .phones { position: absolute; left: 11px; right: 11px; top: 38px; display: flex; justify-content: space-between; }
  .phone { display: flex; align-items: center; }
  .phone .who { font-weight: 700; font-size: 18px; margin-right: 8px; }
  .phone .icon {
    width: 28px; height: 28px; border-radius: 50%; background: var(--band);
    display: flex; align-items: center; justify-content: center; position: relative; z-index: 1;
  }
  .phone .number {
    background: var(--white); border-radius: 14px; height: 26px; line-height: 26px;
    padding: 0 20px 0 22px; margin-left: -10px; font-weight: 600; font-size: 17px;
  }
</style>
</head>
<body>
<main class="flyer">
  <div class="hero-art" role="img" aria-label="Sepia devotional scene inside a chapel: a robed figure bearing a wooden cross on the left and a praying robed statue on the right, bathed in soft golden light"></div>

  <div class="organizer"><span class="mark"></span>Casas de Monte Olvera</div>

  <h1 class="title">JORNADAS</h1>
  <p class="subtitle">en Quietud</p>
  <p class="tagline">Los retiros son mensuales</p>

  <section class="schedule women">
    <span class="audience">PARA MUJERES</span>
    <p class="lead">se realizan el</p>
    <div class="dates">
      <div class="date"><span class="day">21</span><span class="month"><span class="de">DE</span><span class="name">FEBRERO</span></span></div>
      <span class="and">y</span>
      <div class="date"><span class="day">21</span><span class="month"><span class="de">DE</span><span class="name">MARZO</span></span></div>
    </div>
    <p class="cadence">(CADA TERCER SÁBADO)</p>
  </section>

  <section class="schedule men">
    <span class="audience">PARA HOMBRES</span>
    <p class="lead">se realizan el</p>
    <div class="dates">
      <div class="date"><span class="day">28</span><span class="month"><span class="de">DE</span><span class="name">FEBRERO</span></span></div>
      <span class="and">y</span>
      <div class="date"><span class="day">28</span><span class="month"><span class="de">DE</span><span class="name">MARZO</span></span></div>
    </div>
    <p class="cadence">(CADA CUARTO SÁBADO)</p>
  </section>

  <div class="cost">
    <span class="label">El costo<br>es de</span>
    <span class="currency">$</span>
    <span class="amount">80</span>
  </div>

  <div class="divider"></div>

  <div class="venue">
    <h3>LUGAR</h3>
    <div class="address">
      <svg width="22" height="22" viewBox="0 0 22 22" aria-hidden="true">
        <circle cx="11" cy="11" r="11" fill="#7b3b07"/>
        <path d="M11 5a3.6 3.6 0 0 0-3.6 3.6c0 2.6 3.6 6 3.6 6s3.6-3.4 3.6-6A3.6 3.6 0 0 0 11 5z" fill="#fff"/>
        <circle cx="11" cy="8.6" r="1.3" fill="#7b3b07"/>
        <path d="M6.5 16h9" stroke="#fff" stroke-width="1.4" stroke-linecap="round"/>
      </svg>
      <span>Casa de Reposo, 4175<br>Marwick Ln, Falls Church, VA.</span>
    </div>
  </div>

  <section class="contact">
    <div class="heading">Para más información</div>
    <div class="phones">
      <div class="phone">
        <span class="who">Para mujeres</span>
        <span class="icon"><svg width="16" height="16" viewBox="0 0 24 24" aria-hidden="true"><path d="M6.6 10.8a15.1 15.1 0 0 0 6.6 6.6l2.2-2.2a1 1 0 0 1 1-.25 11.4 11.4 0 0 0 3.6.57 1 1 0 0 1 1 1V20a1 1 0 0 1-1 1A17 17 0 0 1 3 4a1 1 0 0 1 1-1h3.5a1 1 0 0 1 1 1c0 1.250.2 2.45.57 3.57a1 1 0 0 1-.25 1z" fill="#fff"/></svg></span>
        <span class="number">540-627-1954</span>
      </div>
      <div class="phone">
        <span class="who">Para hombres</span>
        <span class="icon"><svg width="16" height="16" viewBox="0 0 24 24" aria-hidden="true"><path d="M6.6 10.8a15.1 15.1 0 0 0 6.6 6.6l2.2-2.2a1 1 0 0 1 1-.25 11.4 11.4 0 0 0 3.6.57 1 1 0 0 1 1 1V20a1 1 0 0 1-1 1A17 17 0 0 1 3 4a1 1 0 0 1 1-1h3.5a1 1 0 0 1 1 1c0 1.250.2 2.45.57 3.57a1 1 0 0 1-.25 1z" fill="#fff"/></svg></span>
        <span class="number">571-482-7105</span>
      </div>
    </div>
  </section>
</main>
</body>
</html>
```